Core Value Graphic for a Service Disabled and Minority Certified contractor

My company, Keystone Aid Partners, is a US Federal Contractor that hires veterans and service disabled veterans. Our website is www.keystoneaid7.example. We work hard to maintain a 50:50 split between veterans and non-veterans on our team. Our tagline is "To Find a Better Way." We are continually looking to integrate technology and efficiency into all that we do.

I want a way to express our company core values visually so that our employees and customers alike can read them and get a sense of who we are, what drives us to succeed, and what makes up our team DNA.

I need an artist like you to help me represent our core values visually. In a manner that I can print it out on an 8"X11" sheet of paper or a large 48" X 48" poster, without losing the visual clarity or that it pixelates out of focus. I am looking for a color scheme that is patriotic with Red, White, and Blues and similar hues. I would also like to incorporate my logo and tagline into the design in some manner.

I have attached several examples of a Core Value Grids from other companies. I am hopeful it will inspire you, and a get your brain juices flowing to provide me with a knockout Core Value Grid that will rock only you can provide! I also include a copy of my company Core Values and a copy of our Logo.

Looking forward to seeing your creations. Thanks.

Target Market(s)

Employees, any potential strategic alliance partners, and customers.

Industry/Entity Type

Contractor

Requirements
Must have
• Patriotic feel and have my logo someplace on the document.

```html
<!DOCTYPE html>
<html lang="en">
<head>
<meta charset="utf-8">
<title>Keystone Aid Partners – Core Values</title>
<link href="https://fonts.googleapis.com/css2?family=Exo+2:wght@500;600&family=Montserrat:wght@700;800&family=Roboto+Condensed:wght@400&display=swap" rel="stylesheet">
<style>
  :root {
    --stage: #888888;
    --maroon-deep: #5a0e1b;
    --maroon: #7a1226;
    --red: #a61a33;
    --navy: #17255c;
    --white: #ffffff;
  }
  * { margin: 0; padding: 0; box-sizing: border-box; }
  html, body { width: 1022px; height: 1200px; overflow: hidden; background: var(--stage); }
  .poster {
    position: absolute; left: 174px; top: 123px; width: 674px; height: 953px;
    background:
      radial-gradient(ellipse 520px 420px at 62% 68%, var(--red) 0%, var(--maroon) 55%, var(--maroon-deep) 100%);
    overflow: hidden; color: var(--white);
  }
  .frame { position: absolute; left: 0; top: 0; width: 674px; height: 953px; }
  .value-title {
    position: absolute; font-family: "Exo 2", sans-serif; font-weight: 600;
    font-size: 20px; line-height: 24px; white-space: nowrap;
  }
  .value-body {
    position: absolute; font-family: "Roboto Condensed", sans-serif;
    font-size: 9.2px; line-height: 13px; text-align: justify;
  }
  .value-body p { text-indent: 11px; }
  .value-body.large { font-size: 10px; line-height: 13.6px; }
  .value-body.large p { margin-bottom: 3px; }
  .value-body.wide p { text-indent: 0; margin-bottom: 3px; }
  .tagline, .tagline-sub, .core-title {
    position: absolute; left: 95px; width: 484px; text-align: center;
    font-family: "Montserrat", sans-serif; font-weight: 700; letter-spacing: 1px;
  }
  .tagline { top: 290px; font-size: 40px; line-height: 50px; }
  .tagline-sub { top: 344px; font-size: 26px; line-height: 30px; }
  .core-title { top: 410px; font-size: 50px; line-height: 60px; font-weight: 800; letter-spacing: 0.5px; }
  .brand {
    position: absolute; left: 56px; top: 900px; display: flex; align-items: center; gap: 8px;
    font-family: "Exo 2", sans-serif; font-weight: 600; font-size: 15px; letter-spacing: 0.5px;
  }
  .brand-square { width: 14px; height: 14px; background: var(--white); }
  .site-url {
    position: absolute; left: 509px; top: 928px; font-family: "Roboto Condensed", sans-serif;
    font-size: 11.5px; line-height: 14px;
  }
</style>
</head>
<body>
<main class="poster">
  <svg class="frame" viewBox="0 0 674 953" aria-hidden="true">
    <g fill="none" stroke="#ffffff" stroke-width="1.6">
      <polyline points="32,53 32,289 95,289"/>
      <polyline points="588,56 640,56 640,289 579,289"/>
      <rect x="95" y="267" width="484" height="174" rx="10" fill="rgba(90,10,25,0.25)"/>
      <polyline points="32,475 32,351 95,351"/>
      <polyline points="55,530 55,415 127,415"/>
      <polyline points="547,415 640,415 640,535 559,535"/>
    </g>
    <g fill="#ffffff">
      <circle cx="32" cy="53" r="3.5"/>
      <circle cx="588" cy="56" r="3.5"/>
      <circle cx="55" cy="530" r="3.5"/>
      <circle cx="559" cy="535" r="3.5"/>
      <circle cx="32" cy="745" r="3.5"/>
      <line x1="32" y1="475" x2="32" y2="745" stroke="#ffffff" stroke-width="1.6"/>
    </g>
    <polygon points="133,401 547,401 532,440 547,477 127,477 141,440" fill="var(--navy)"/>
    <g fill="#ffffff">
      <polygon id="star" points="0,-10 2.9,-3.1 9.5,-3.1 4.2,1.6 5.9,8.5 0,4.5 -5.9,8.5 -4.2,1.6 -9.5,-3.1 -2.9,-3.1" transform="translate(147,317)"/>
      <use href="#star" x="34"/><use href="#star" x="68"/>
      <use href="#star" x="391"/><use href="#star" x="425"/><use href="#star" x="459"/>
    </g>
    <rect x="0" y="943" width="674" height="10" fill="var(--navy)"/>
    <polygon points="478,915 674,915 674,953 452,953" fill="var(--navy)"/>
  </svg>

  <h2 class="value-title" style="left:56px;top:40px;">Everyone comes back to<br>the Green Zone.</h2>
  <div class="value-body" style="left:56px;top:99px;width:269px;">
    <p>WHAT IT MEANS- Safety takes precedence over every phase of the day's operation.</p>
    <p>HOW TO EXPRESS IT - Anyone can call a stop to the work in progress if an unsafe act is occurring. In fact, it is each team member's duty to do so, rectify the unsafe issue, then proceed. Never hesitate; everyone comes back. Finally, each After Action Review begins with discussing safety issues.</p>
    <p>We always let everyone on the team know of an unsafe situation, so it can be avoided in the future.</p>
    <p>RESULT - All team members go home to their loved ones each day to pursue their individual happiness.</p>
  </div>

  <h2 class="value-title" style="left:348px;top:44px;">Boldly go. Seek. Find.</h2>
  <div class="value-body" style="left:348px;top:99px;width:269px;">
    <p>WHAT IT MEANS: - We weave innovation into the fabric that makes up our company.</p>
    <p>HOW TO EXPRESS IT: - We're early adopters of technology. We quickly evaluate new technologies or processes that could separate us from our competition. Then we implement and evaluate these new technologies. We dump it quickly if we see it is not helping us achieve "Commander's Intent." We have the guts to be first. We iterate continuously and attack, attack, attack.</p>
    <p>RESULT: - We will be ahead of our competition. It' one mechanism that helps us scale. Prosperity favors the bold!</p>
  </div>

  <div class="tagline">TO FIND</div>
  <div class="tagline-sub">A BETTER WAY</div>
  <h1 class="core-title">CORE VALUES</h1>

  <h2 class="value-title" style="left:68px;top:519px;">Never leave your wingman</h2>
  <div class="value-body large" style="left:56px;top:562px;width:268px;">
    <p>WHAT IT MEANS – We always help your team members be successful. Commitment to each other and to our own personal integrity is the fuel that empowers us.</p>
    <p>HOW TO EXPRESS IT – If a Wingman is having challenges accomplishing their individual priorities or completing their assigned mission, volunteer to help them to do so.</p>
    <p>This goes for Subs/Suppliers as well. We help those who help us succeed! Always look to establish the best win-win relationship possible, and do what you can to support them if they get into a bind.</p>
    <p>RESULT – Be there for them and they will be there for us.</p>
  </div>

  <h2 class="value-title" style="left:349px;top:519px;">Fail quickly and learn</h2>
  <div class="value-body large" style="left:349px;top:562px;width:268px;">
    <p>WHAT IT MEANS – If you're not making mistakes, you're not taking enough chances or getting out of your comfort zone.</p>
    <p>HOW TO EXPRESS IT – Use your best judgment when trying something new. But, don't let your pride keep you from saying, "I was wrong" when your idea doesn't work. We trust you will know when it's time to dump the idea, or stop doing something that doesn't work.</p>
    <p>RESULT – No one will ever be penalized for making a mistake. Don't be afraid to try something you believe will work. That's how we grow ourselves and our team members.</p>
  </div>

  <h2 class="value-title" style="left:56px;top:736px;">Troops (Team Members)&nbsp; eat first</h2>
  <div class="value-body large wide" style="left:56px;top:775px;width:561px;">
    <p>WHAT IT MEANS – No leader will put themselves ahead of their subordinates.</p>
    <p>HOW TO EXPRESS IT – We lead by example. Demonstrate the moral courage and discipline to do the right thing at the highest level of quality.</p>
    <p>RESULT – Every new teammember's will quickly realize their leaders genuinely care for their welfare and success. This is the best way to drive Esprit de Corps and achieve excellence.</p>
  </div>

  <div class="brand"><span class="brand-square"></span><span>KEYSTONE AID PARTNERS</span></div>
  <div class="site-url">www.keystoneaid7.example</div>
</main>
</body>
</html>
```